Communication Business Card Design

We offer complete cabling solutions
Data Cabling,Fibre Optic, and Cabling Repairs fault finding
Security camera installation
TV Aerial installation
Security alarm installation
QWV

Industry/Entity Type

Business

Contact Information for Business Card

Threadmore Solutions
ABN 52 918 374 260
EMAIL threadmoresolutions.com.au
Mobile 0418362057
Rob Kesler

```html
<!DOCTYPE html>
<html lang="en">
<head>
<meta charset="utf-8">
<title>Threadmore Solutions – Business Card</title>
<link rel="stylesheet" href="https://fonts.googleapis.com/css2?family=Exo+2:wght@500;600&family=Share+Tech+Mono&family=Inter:wght@400;600;700&display=swap">
<style>
  :root {
    --page-bg: #e6e7e8;
    --front-deep: #03060f;
    --front-navy: #0c1a44;
    --brand-blue: #4ab6ee;
    --tagline-blue: #3ea3dc;
    --back-light: #ffffff;
    --back-shade: #dcdcdc;
    --ink-dark: #2b2b2b;
    --ink-mid: #4a4a4a;
    --swoosh-magenta: #d1207a;
    --swoosh-yellow: #f6c514;
    --swoosh-violet: #5a3fb5;
    --swoosh-cyan: #3fa9d8;
  }
  * { margin: 0; padding: 0; box-sizing: border-box; }
  html, body { width: 1200px; height: 900px; overflow: hidden; }
  body {
    background: var(--page-bg);
    display: flex;
    align-items: center;
    justify-content: center;
    gap: 60px;
  }
  .card {
    position: relative;
    width: 500px;
    height: 286px;
    overflow: hidden;
    box-shadow: 0 6px 18px rgba(0,0,0,0.18);
  }

  /* Front side */
  .card--front {
    background: radial-gradient(ellipse at 60% 40%, var(--front-navy) 0%, var(--front-deep) 75%);
  }
  .cable-art {
    position: absolute;
    left: 0; top: 88px;
    width: 400px; height: 150px;
    background:
      radial-gradient(ellipse at 55% 50%, rgba(80,170,255,0.55) 0%, rgba(30,80,180,0.25) 40%, transparent 70%),
      linear-gradient(100deg, #1b1d22 0%, #3a3d44 35%, rgba(40,60,120,0.4) 60%, transparent 100%);
    border-radius: 0 80px 80px 0;
  }
  .brand {
    position: absolute;
    left: 58px; top: 28px;
    font-family: "Exo 2", sans-serif;
    color: var(--brand-blue);
    line-height: 1;
  }
  .brand__name {
    display: block;
    font-size: 38px;
    font-weight: 600;
    letter-spacing: 3px;
  }
  .brand__suffix {
    display: block;
    text-align: right;
    font-size: 21px;
    font-weight: 500;
    letter-spacing: 4px;
    margin-top: 2px;
  }
  .tagline {
    position: absolute;
    left: 0; right: 0; bottom: 22px;
    text-align: center;
    font-family: "Share Tech Mono", monospace;
    font-size: 11.5px;
    letter-spacing: 1.2px;
    line-height: 1.6;
    color: var(--tagline-blue);
  }

  /* Back side */
  .card--back {
    background: linear-gradient(160deg, var(--back-light) 0%, #f1f1f1 45%, var(--back-shade) 100%);
    font-family: "Inter", sans-serif;
  }
  .holder {
    position: absolute;
    left: 48px; top: 46px;
  }
  .holder__name {
    font-size: 25px;
    font-weight: 700;
    letter-spacing: 1.5px;
    color: var(--ink-dark);
  }
  .holder__role {
    font-size: 13px;
    color: var(--ink-mid);
    margin-left: 34px;
    margin-top: -2px;
  }
  .swoosh-art {
    position: absolute;
    left: 48px; top: 130px;
    width: 200px; height: 156px;
    background:
      radial-gradient(ellipse at 100% 0%, var(--swoosh-cyan) 0%, var(--swoosh-violet) 25%, transparent 50%),
      linear-gradient(40deg, var(--swoosh-yellow) 0%, #ef6a2a 30%, var(--swoosh-magenta) 60%, var(--swoosh-violet) 100%);
    border-radius: 0 160px 0 0;
  }
  .company {
    position: absolute;
    left: 252px; top: 132px;
    color: var(--ink-dark);
  }
  .company__name { font-size: 14.5px; font-weight: 700; }
  .company__abn { font-size: 10.5px; color: var(--ink-mid); margin-left: 10px; margin-top: 2px; }
  .contact {
    position: absolute;
    left: 258px; top: 198px;
    list-style: none;
    font-size: 11.5px;
    color: var(--ink-mid);
  }
  .contact__item { display: flex; align-items: center; gap: 7px; margin-bottom: 4px; }
  .contact__icon { width: 9px; height: 11px; }
</style>
</head>
<body>
  <section class="card card--front">
    <div class="cable-art" role="img" aria-label="Fibre optic cable with coloured cores and glowing light strands"></div>
    <h1 class="brand">
      <span class="brand__name">Threadmore</span>
      <span class="brand__suffix">Solutions</span>
    </h1>
    <p class="tagline">Data Cabling,Fibre Optic, and Cabling Repairs fault finding<br>Security camera installation</p>
  </section>

  <section class="card card--back">
    <div class="holder">
      <h2 class="holder__name">Rob Kesler</h2>
      <p class="holder__role">general manager</p>
    </div>
    <div class="swoosh-art" role="img" aria-label="Colourful sweeping ribbon in magenta, yellow and violet"></div>
    <div class="company">
      <p class="company__name">Threadmore Solutions</p>
      <p class="company__abn">ABN 52 918 374 260</p>
    </div>
    <ul class="contact">
      <li class="contact__item">
        <svg class="contact__icon" viewBox="0 0 9 11" aria-hidden="true"><rect x="1" y="0.5" width="7" height="10" rx="1.3" fill="none" stroke="#333" stroke-width="1"/><rect x="3" y="8.3" width="3" height="0.9" fill="#333"/></svg>
        <span>0418362057</span>
      </li>
      <li class="contact__item">
        <svg class="contact__icon" viewBox="0 0 9 11" aria-hidden="true"><circle cx="4.5" cy="5.5" r="4" fill="#333"/><path d="M0.5 5.5h8M4.5 1.5c-2 2.5-2 5.5 0 8M4.5 1.5c2 2.5 2 5.5 0 8" stroke="#fff" stroke-width="0.7" fill="none"/></svg>
        <span>threadmoresolutions.com.au</span>
      </li>
    </ul>
  </section>
</body>
</html>
```